Creative Design "Size Chart" for a Clothing Product

Hi, My dear friends! I am looking to do a contest to design a unique creative "Size Chart" for our clothing line. See Attached the Sizes & Ideas Thanks Good Luck Dolph

Colors

Designer to choose colors to be used in the design.

```html
<!DOCTYPE html>
<html lang="en">
<head>
<meta charset="utf-8">
<title>Size Chart</title>
<link rel="stylesheet" href="https://fonts.googleapis.com/css2?family=Montserrat:wght@300;400;600;700;800&family=Arimo:wght@400&family=Oswald:wght@400&display=swap">
<style>
  :root {
    --page: #3d3d3d;
    --blue: #0097d9;
    --pink: #f5aeb1;
    --yellow: #fff111;
    --ink: #3a3a3a;
    --navy: #4f5f8a;
    --violet: #7b76b8;
    --white: #ffffff;
  }
  * { margin: 0; padding: 0; box-sizing: border-box; }
  html, body { width: 682px; height: 1200px; overflow: hidden; background: var(--page); }
  body { position: relative; font-family: "Montserrat", sans-serif; }

  .chart { position: absolute; left: 75px; width: 532px; height: 497px; overflow: hidden; }
  .chart--men { top: 71px; background: var(--blue); }
  .chart--women { top: 618px; background: var(--pink); }
  .chart > * { position: absolute; }

  .chart__title { font-weight: 800; line-height: 1; letter-spacing: -0.5px; }
  .chart--men .chart__title { left: 26px; top: 18px; font-size: 68px; color: var(--white); }
  .chart--women .chart__title { left: 25px; top: 18px; font-size: 66px; color: var(--navy); }

  .chart__subtitle { font-weight: 700; font-size: 22px; line-height: 1; top: 26px; }
  .chart--men .chart__subtitle { left: 259px; color: var(--yellow); }
  .chart--women .chart__subtitle { left: 382px; color: var(--ink); }

  .chart__rule { height: 5px; background: var(--yellow); top: 48px; right: 0; }
  .chart--men .chart__rule { left: 257px; }
  .chart--women .chart__rule { left: 384px; }

  .chart__unit { font-weight: 400; font-size: 11px; line-height: 1; top: 61px; }
  .chart--men .chart__unit { left: 332px; color: var(--yellow); }
  .chart--women .chart__unit { left: 454px; top: 64px; color: var(--ink); }

  .brand-badge {
    width: 168px; height: 168px; border-radius: 50%; background: var(--yellow);
    display: flex; align-items: center; justify-content: center; text-align: center;
    font-weight: 400; font-size: 22px; line-height: 1.05; color: var(--ink);
  }
  .chart--men .brand-badge { left: 336px; top: 81px; }
  .chart--women .brand-badge { left: 336px; top: 66px; }

  .figure { background: linear-gradient(180deg, #ffffff 0%, #f6f8fa 100%); border-radius: 90px 90px 6px 6px; }
  .chart--men .figure { left: 171px; top: 84px; width: 188px; height: 413px; }
  .chart--women .figure { left: 169px; top: 80px; width: 190px; height: 417px; }

  .guides { left: 0; top: 0; width: 532px; height: 497px; }
  .guides .leader { stroke: var(--white); stroke-width: 1.4; fill: none; }
  .guides .measure { stroke: var(--ink); stroke-width: 1.2; fill: none; }
  .guides .measure-label { font-family: "Montserrat", sans-serif; font-weight: 300; font-size: 20px; fill: var(--ink); text-anchor: middle; }

  .col-head { font-weight: 700; font-size: 10.5px; line-height: 1; }
  .chart--men .col-head { color: var(--yellow); }
  .chart--women .col-head { color: var(--ink); }

  .size {
    width: 28px; height: 28px; border-radius: 50%; margin-left: -14px; margin-top: -14px;
    display: flex; align-items: center; justify-content: center;
    color: var(--white); font-weight: 700; font-size: 17px; letter-spacing: -0.5px;
  }
  .chart--men .size { background: var(--ink); }
  .chart--women .size { background: var(--violet); width: 27px; height: 27px; margin-left: -13.5px; margin-top: -13.5px; font-size: 15px; }
  .range { font-weight: 600; font-size: 14px; line-height: 1; margin-top: -7px; letter-spacing: 0.3px; }
  .chart--men .range { color: var(--white); }
  .chart--women .range { color: var(--ink); }

  .intro__title { font-family: "Oswald", sans-serif; font-weight: 400; font-size: 14px; line-height: 1; letter-spacing: -0.4px; }
  .intro__body { font-family: "Arimo", sans-serif; font-size: 10.3px; line-height: 12.3px; width: 140px; letter-spacing: -0.1px; }
  .chart--men .intro__title { color: var(--yellow); left: 24px; top: 339px; }
  .chart--men .intro__body { color: var(--white); left: 24px; top: 356px; }
  .chart--women .intro__title { color: var(--ink); left: 23px; top: 337px; }
  .chart--women .intro__body { color: var(--ink); left: 23px; top: 355px; }
</style>
</head>
<body>

<section class="chart chart--men">
  <div class="figure" role="img" aria-label="White silhouette of a male torso showing where chest and waist are measured"></div>
  <svg class="guides" viewBox="0 0 532 497" aria-hidden="true">
    <polyline class="leader" points="134,157 134,319"/>
    <polyline class="leader" points="134,249 150,249 171,253"/>
    <polyline class="leader" points="381,305 381,466"/>
    <polyline class="leader" points="310,355 365,376 381,376"/>
    <text class="measure-label" x="261" y="257">CHEST</text>
    <path class="measure" d="M202,258 Q259,268 317,258"/>
    <path class="measure" d="M310,255 L317,258 L310,261 M255,261 L261,263.5 L255,266"/>
    <text class="measure-label" x="261" y="334">WAIST</text>
    <path class="measure" d="M209,336 Q259,346 309,336"/>
    <path class="measure" d="M302,333 L309,336 L302,339 M255,339 L261,341.5 L255,344"/>
  </svg>
  <h1 class="chart__title">MANS</h1>
  <div class="chart__subtitle">SIZE CHART</div>
  <div class="chart__rule"></div>
  <div class="chart__unit">IN INCHES</div>
  <div class="brand-badge">logo /<br>brand</div>

  <div class="col-head" style="left:36px;top:151px">SIZE</div>
  <div class="col-head" style="left:76px;top:151px">CHEST</div>
  <div class="size" style="left:48px;top:182px">S</div><div class="range" style="left:74px;top:182px">34-36</div>
  <div class="size" style="left:48px;top:222px">M</div><div class="range" style="left:74px;top:222px">36-38</div>
  <div class="size" style="left:48px;top:262px">L</div><div class="range" style="left:74px;top:262px">38-40</div>
  <div class="size" style="left:48px;top:303px">XL</div><div class="range" style="left:74px;top:303px">40-42</div>

  <div class="col-head" style="left:406px;top:303px">SIZE</div>
  <div class="col-head" style="left:449px;top:303px">WAIST</div>
  <div class="size" style="left:418px;top:333px">S</div><div class="range" style="left:446px;top:333px">28-30</div>
  <div class="size" style="left:418px;top:374px">M</div><div class="range" style="left:446px;top:374px">30-32</div>
  <div class="size" style="left:418px;top:414px">L</div><div class="range" style="left:446px;top:414px">32-34</div>
  <div class="size" style="left:418px;top:455px">XL</div><div class="range" style="left:446px;top:455px">34-36</div>

  <div class="intro__title">Introducing</div>
  <p class="intro__body">Lorem ipsum dolor sit amet, consectetur adipiscing elit, sed do eiusmod tempor incididunt ut labore et dolore magna aliqua. Ut enim ad minim veniam, quis nostrud exercitation ullamco laboris nisi ut aliquip ex ea commodo</p>
</section>

<section class="chart chart--women">
  <div class="figure" role="img" aria-label="White silhouette of a female torso showing where chest and waist are measured"></div>
  <svg class="guides" viewBox="0 0 532 497" aria-hidden="true">
    <polyline class="leader" points="132,110 132,318"/>
    <polyline class="leader" points="132,249 148,249 174,259"/>
    <polyline class="leader" points="381,306 381,466"/>
    <polyline class="leader" points="316,366 348,374 381,374"/>
    <text class="measure-label" x="262" y="271">CHEST</text>
    <path class="measure" d="M202,271 Q258,281 315,271"/>
    <path class="measure" d="M308,268 L315,271 L308,274 M256,274 L262,276.5 L256,279"/>
    <text class="measure-label" x="266" y="347">WAIST</text>
    <path class="measure" d="M218,353 Q266,363 313,353"/>
    <path class="measure" d="M306,350 L313,353 L306,356 M260,356 L266,358.5 L260,361"/>
  </svg>
  <h1 class="chart__title">WOMENS</h1>
  <div class="chart__subtitle">SIZE CHART</div>
  <div class="chart__rule"></div>
  <div class="chart__unit">IN INCHES</div>
  <div class="brand-badge">logo /<br>brand</div>

  <div class="col-head" style="left:28px;top:90px">SIZE</div>
  <div class="col-head" style="left:72px;top:90px">CHEST</div>
  <div class="size" style="left:40px;top:115px">XS</div><div class="range" style="left:70px;top:115px">32-34</div>
  <div class="size" style="left:40px;top:150px">S</div><div class="range" style="left:70px;top:150px">34-36</div>
  <div class="size" style="left:40px;top:182px">M</div><div class="range" style="left:70px;top:182px">36-38</div>
  <div class="size" style="left:40px;top:216px">L</div><div class="range" style="left:70px;top:216px">38-40</div>
  <div class="size" style="left:40px;top:249px">XL</div><div class="range" style="left:70px;top:249px">40-42</div>
  <div class="size" style="left:40px;top:282px">2X</div><div class="range" style="left:70px;top:282px">42-44</div>
  <div class="size" style="left:40px;top:317px">3X</div><div class="range" style="left:70px;top:317px">44-46</div>

  <div class="col-head" style="left:405px;top:246px">SIZE</div>
  <div class="col-head" style="left:449px;top:246px">WAIST</div>
  <div class="size" style="left:417px;top:271px">XS</div><div class="range" style="left:446px;top:271px">26-28</div>
  <div class="size" style="left:417px;top:306px">S</div><div class="range" style="left:446px;top:306px">28-30</div>
  <div class="size" style="left:417px;top:338px">M</div><div class="range" style="left:446px;top:338px">30-32</div>
  <div class="size" style="left:417px;top:372px">L</div><div class="range" style="left:446px;top:372px">32-34</div>
  <div class="size" style="left:417px;top:406px">XL</div><div class="range" style="left:446px;top:406px">34-36</div>
  <div class="size" style="left:417px;top:439px">2X</div><div class="range" style="left:446px;top:439px">36-38</div>
  <div class="size" style="left:417px;top:473px">3X</div><div class="range" style="left:446px;top:473px">38-40</div>

  <div class="intro__title">Introducing</div>
  <p class="intro__body">Lorem ipsum dolor sit amet, consectetur adipiscing elit, sed do eiusmod tempor incididunt ut labore et dolore magna aliqua. Ut enim ad minim veniam, quis nostrud exercitation ullamco laboris nisi ut aliquip ex ea commodo</p>
</section>

</body>
</html>
```